Harrowgate Estates Business Card for Apartment Buildings

Create business cards for resident managers who run apartment buildings. The audience is the public who are searching for apartment rentals, and current residents who live at the apartment building. Key design element will be incorporating the company logo, however, the logo cannot dominate. The building name and manager name are more important than the logo. Current business card design leaves little room for copy, so we may need to reduce the size on the current card to allow for more space for copy.

Target Market(s)

Adults 18-65 years of age, who are looking for an apartment rental, plus current residents who live at our apartment buildings.

Industry/Entity Type

Property Management

Contact Information for Business Card

A major design element will be use of the company logo. Important property and manager contact information must be part of the design. The size of the logo will need to be reduced to make room for building and manager contact copy.

Font styles to use
Sans Serif

Colors
3176b5
000000
959595
ffffff

Requirements
Must have
• 1) Incorporate the company logo.
• 2) Use the company colors (dark blue, black/grey, over white).
• 3) FEATURE THE BUILDING NAME
• 4) FEATURE THE MANAGER NAME
• 5) The company name is less important than BUILDING and MANAGER
• 6) Manager contact information
• **SEE ATTACHED CREATIVE BRIEF**
Nice to have
• 1) Back of card logo watermark
• 2) Ability to write notes on back of carfd
Should not have
• Avoid letting the company logo dominate the card, the building name and manager are more important than the company logo.

```html
<!DOCTYPE html>
<html lang="en">
<head>
<meta charset="utf-8">
<title>Harrowgate Estates – Business Card</title>
<link href="https://fonts.googleapis.com/css2?family=Oswald:wght@500&family=Roboto:wght@400;700&display=swap" rel="stylesheet">
<style>
  :root {
    --brand-blue: #20649a;
    --brand-blue-light: #3176b5;
    --ink: #1b1b1b;
    --swoosh: #3a3d40;
    --paper: #f4f4f4;
    --white: #ffffff;
    --stage: #e4e4e4;
  }
  * { box-sizing: border-box; margin: 0; padding: 0; }
  html, body { width: 1200px; height: 726px; overflow: hidden; }
  body {
    background: var(--stage);
    font-family: "Roboto", Arial, sans-serif;
    position: relative;
  }
  .card {
    position: absolute;
    top: 208px;
    width: 540px;
    height: 309px;
    overflow: hidden;
    box-shadow: 0 2px 6px rgba(0,0,0,.12);
  }
  .card--front { left: 40px; background: var(--brand-blue); color: var(--white); }
  .card--back { left: 620px; background: var(--paper); color: var(--ink); }

  /* Front */
  .front-logo {
    position: absolute;
    left: 0; right: 0; top: 98px;
    display: flex; align-items: center; justify-content: center; gap: 12px;
  }
  .logo-square { width: 30px; height: 30px; background: currentColor; }
  .logo-name {
    font-weight: 700;
    line-height: 1;
  }
  .logo-name .line1 { display: block; font-size: 34px; letter-spacing: 1px; text-transform: uppercase; }
  .logo-name .line2 { display: block; font-size: 13px; letter-spacing: 5px; text-transform: uppercase; margin-top: 4px; }
  .front-web {
    position: absolute; left: 0; right: 0; bottom: 40px;
    text-align: center; font-size: 14px; letter-spacing: .3px;
  }

  /* Back */
  .wave { position: absolute; inset: 0; }
  .manager {
    position: absolute; right: 28px; top: 26px; text-align: right; color: var(--white);
  }
  .manager-name {
    font-family: "Oswald", "Arial Narrow", sans-serif;
    font-weight: 500; font-size: 28px; letter-spacing: .5px; line-height: 1;
    text-transform: uppercase;
  }
  .manager-title { font-size: 14px; margin-top: 4px; }
  .back-logo {
    position: absolute; left: 30px; top: 150px;
    display: flex; align-items: center; gap: 10px; color: var(--brand-blue);
  }
  .back-logo .logo-square { width: 24px; height: 24px; }
  .back-logo .line1 { font-size: 28px; }
  .back-logo .line2 { font-size: 11px; letter-spacing: 4px; }
  .contacts {
    position: absolute; left: 30px; bottom: 20px;
    list-style: none; font-size: 13.5px; line-height: 18px;
  }
  .contacts li { display: flex; align-items: center; gap: 10px; }
  .contacts svg { width: 12px; height: 12px; fill: var(--brand-blue); flex: none; }
  .contacts .web-accent { color: var(--brand-blue-light); }
  .address {
    position: absolute; right: 28px; top: 210px;
    font-size: 13.5px; line-height: 18px; text-align: right;
  }
</style>
</head>
<body>

<section class="card card--front">
  <div class="front-logo">
    <span class="logo-square"></span>
    <span class="logo-name"><span class="line1">Harrowgate</span><span class="line2">Estates LLC</span></span>
  </div>
  <p class="front-web">www.harrowgateestates.us</p>
</section>

<section class="card card--back">
  <svg class="wave" viewBox="0 0 540 309" preserveAspectRatio="none" aria-hidden="true">
    <path d="M0 0 H540 V92 C450 108 380 140 300 146 C210 152 120 118 0 120 Z" fill="var(--brand-blue)"/>
    <path d="M0 120 C120 118 210 152 300 146 C380 140 450 108 540 92 V104 C450 122 380 158 300 164 C200 170 110 132 0 134 Z" fill="var(--swoosh)"/>
  </svg>

  <div class="manager">
    <p class="manager-name">Dana Whitlow</p>
    <p class="manager-title">Property Manager</p>
  </div>

  <div class="back-logo">
    <span class="logo-square"></span>
    <span class="logo-name"><span class="line1">Harrowgate</span><span class="line2">Estates LLC</span></span>
  </div>

  <ul class="contacts">
    <li><svg viewBox="0 0 12 12"><path d="M2.5 0.5 L4.5 2.5 L3.5 4 C4.3 5.6 6.4 7.7 8 8.5 L9.5 7.5 L11.5 9.5 L10 11.5 C5 11 1 7 0.5 2 Z"/></svg>555-014-2231</li>
    <li><svg viewBox="0 0 12 12"><path d="M3 0 H9 V3 H3 Z M0 4 H12 V9 H10 V7 H2 V9 H0 Z M3 8 H9 V12 H3 Z"/></svg>555-014-7790</li>
    <li><svg viewBox="0 0 12 12"><path d="M0 2 H12 V10 H0 Z M1 3 L6 7 L11 3" fill="none" stroke="var(--brand-blue)" stroke-width="1.2"/></svg>dana@harrowgateestates.us</li>
    <li><svg viewBox="0 0 12 12"><circle cx="6" cy="6" r="5.3" fill="none" stroke="var(--brand-blue)" stroke-width="1.2"/><path d="M0.7 6 H11.3 M6 0.7 C3 3.5 3 8.5 6 11.3 M6 0.7 C9 3.5 9 8.5 6 11.3" fill="none" stroke="var(--brand-blue)" stroke-width="1"/></svg>www.<span class="web-accent">harrowgateestates</span>.us</li>
  </ul>

  <p class="address">1820 Larkspur Valley Road<br>#B210 Fairhaven, CA 90210</p>
</section>

</body>
</html>
```